House-share and Room Rental Website (With Focus on the Bedroom Landing Page)

Looking for website design for our House-share (executive accommodation) and room rental business.

Our company name is: Lodvenra could also be written as LodVenra or lodvenra. Either is fine .. just looking for a nice clean catchy logo to go with the design.

EXAMPLES
These are examples of other websites in this field that are doing well. this is a kind of baseline.
https://kelbrin.com.au/
https://www.tuvaplex.com/
https://www.nestorvi.com/
https://www.quillsa.net/
https://www.pendlebarrow.com.au/

Our business model is to rent rooms to people looking for high-quality accommodation. We fill the gap between those looking to rent rooms and those with rooms to rent. However, our model is slightly different from those already on the market as we looking to fill a massive gap in the market delivering upmarket rooms for rent.(Executive Accommodation) also in the back end will be coupled with a self management process in the back end.

We offer executive style accommodation that stands out above the rest. With special extras like fire safety.. and management processes that create happier homes. We are looking for a web design package that can help us grow and scale our business. We need a design that is captivating

Our MAIN focus is having a room landing page that stands out from the rest... The core of our business will rely on the promotion of the rooms in a share house... so the whole design relies on the BEDROOM landing page to drive results.

Target Market(s)

We have 2 markets we are aiming at ... the first market is people offering rooms to rent who want the highest rental return. The second market is people looking to rent safe, high-quality rooms, in houses that are well managed and looked after.

Industry/Entity Type

Share Economy

Logo Text

LodVenra

Number of Pages Required

5+ page

Font styles to use
Sans Serif

Colors
3276b5

Requirements
Must have
• A messaging system whereby we can create direct communication between those offering rooms and those looking for rooms.
• A call to action that says " Schedule an Inspection"
• Landing page for promoting rooms
• A home page for showing stock.
• Profile page for those selling rooms
• Profile page for those looking for rooms.
• A scheduling calendar for booking inspections
Nice to have
• Pages where new residents can lock in a room.. pay bond and rents.. and sign contracts
• Notifications
• SMS capabilities in the backend.
Should not have
• No script or handwriting fonts.

```html
<!DOCTYPE html>
<html lang="en">
<head>
<meta charset="utf-8">
<title>Lodvenra – 1 BK Sharing Room</title>
<link href="https://fonts.googleapis.com/css2?family=Questrial&display=swap" rel="stylesheet">
<style>
:root{
  --blue:#3276b5;
  --orange:#f0a44a;
  --ink:#2b2b2b;
  --muted:#6b6b6b;
  --line:#dcdcdc;
  --panel:#f2f4f8;
  --footer:#2a2627;
  --field:#5b5859;
  --icon:#4a4a4a;
}
*{box-sizing:border-box;margin:0;padding:0}
html,body{width:679px;height:1200px;overflow:hidden;background:#fff}
body{position:relative;font-family:"Questrial",sans-serif;color:var(--ink)}
h1,h2,h3{font-weight:normal}
a{color:inherit;text-decoration:none}

/* header */
.site-header{position:absolute;left:0;top:0;width:679px;height:45px;background:#fff}
.brand{position:absolute;left:50px;top:9px}
.brand-name{display:flex;align-items:center;gap:4px;font-size:14px;color:var(--blue)}
.brand-mark{width:9px;height:9px;border-radius:50%;background:var(--blue)}
.brand-tag{font-size:6px;color:#9a9a9a;margin-top:3px}
.btn{position:absolute;top:14px;height:17px;border:1px solid var(--blue);border-radius:2px;font-size:7px;display:flex;align-items:center;justify-content:center;gap:4px}
.btn-icon{left:408px;width:18px;height:18px}
.btn-login{left:434px;width:82px;background:var(--blue);color:#fff}
.btn-schedule{left:525px;width:104px;color:var(--blue)}

/* gallery */
.gallery{position:absolute;top:45px;left:0;width:679px;height:204px}
.photo{position:absolute;top:0;height:204px}
.photo-kitchen{left:0;width:113px;background:linear-gradient(160deg,#d9dcd8,#8f8b86 70%,#5a4c40)}
.photo-bedroom{left:116px;width:448px;background:linear-gradient(170deg,#d8c9a2 0%,#e9e1cb 35%,#c9a46a 60%,#7a5a3a 100%)}
.photo-wall{left:566px;width:113px;background:linear-gradient(180deg,#b8b5ac,#8e8b83)}
.arrow{position:absolute;top:91px;width:18px;height:22px;background:#fff;display:flex;align-items:center;justify-content:center}
.arrow-left{left:0;border-radius:0 11px 11px 0}
.arrow-right{right:0;border-radius:11px 0 0 11px}

/* listing */
.listing{position:absolute;left:50px;top:292px;width:412px}
.address{display:flex;align-items:center;gap:4px;font-size:7px;color:var(--muted)}
.map-link{position:absolute;right:0;top:1px;font-size:6px;color:var(--blue);text-decoration:underline}
.listing-title{font-size:10.5px;line-height:13px;margin-top:9px;width:250px}
.listing-meta{font-size:7px;color:var(--muted);margin-top:10px}
.price{font-size:8px;color:var(--blue);margin-top:12px}
.price span{color:var(--orange)}
.rule{position:absolute;left:50px;width:412px;height:1px;background:var(--line)}
.section-title{position:absolute;font-size:9.5px}
.amenity{position:absolute;width:90px;margin-left:-45px;text-align:center;font-size:7px;color:var(--ink)}
.amenity svg{display:block;margin:0 auto 6px}
.room-item{position:absolute;display:flex;align-items:center;gap:10px;font-size:7px}
.room-item svg{flex:none}

/* sidebar */
.sidebar{position:absolute;left:480px;top:313px;width:150px;height:389px;background:var(--panel)}
.avatar{position:absolute;left:526px;top:292px;width:56px;height:56px;border-radius:50%;background:#fff;border:1px solid var(--line);display:flex;align-items:center;justify-content:center}
.avatar-photo{width:46px;height:46px;border-radius:50%;background:radial-gradient(circle at 50% 40%,#e7c3a4,#8a5a3a)}
.host-name{position:absolute;left:480px;width:150px;top:358px;text-align:center;font-size:10px}
.host-role{position:absolute;left:480px;width:150px;top:371px;text-align:center;font-size:7px;color:var(--muted)}
.message-box{position:absolute;left:498px;top:396px;width:113px;height:94px;background:#fff;border:1px solid #e3e6ec;padding:8px;font-size:7px;color:var(--muted)}
.btn-send{position:absolute;left:498px;top:501px;width:113px;height:17px;background:var(--blue);color:#fff;font-size:7px;display:flex;align-items:center;justify-content:center;gap:4px;border-radius:1px}
.side-rule{position:absolute;left:480px;width:150px;height:1px;background:#dfe2e8}
.side-title{position:absolute;left:480px;width:150px;text-align:center;font-size:10px}
.side-text{position:absolute;left:480px;width:150px;text-align:center;font-size:8px}
.side-text a{text-decoration:underline;font-size:7.5px}
.share-box{position:absolute;top:654px;width:17px;height:17px;border:1px solid var(--blue);background:#fff;display:flex;align-items:center;justify-content:center}
.share-box i{width:5px;height:5px;background:var(--blue);display:block}

/* public amenities */
.area-map{position:absolute;left:0;top:810px;width:679px;height:136px;background:linear-gradient(90deg,#e9e9e9,#f1f1f1 45%,#ececec)}

/* footer */
.site-footer{position:absolute;left:0;top:946px;width:679px;height:254px;background:var(--footer);color:#fff}
.f-heading{position:absolute;top:49px;font-size:11px}
.f-phone{position:absolute;left:50px;top:72px;font-size:13px;color:#d8d8d8}
.f-small{position:absolute;font-size:7px;color:#a9a6a6;line-height:10px}
.f-link{position:absolute;left:50px;top:132px;font-size:7px;color:var(--blue);text-decoration:underline}
.f-social{position:absolute;top:172px;width:18px;height:18px;border:1px solid var(--blue);display:flex;align-items:center;justify-content:center}
.f-social.active{background:var(--blue)}
.f-social i{width:5px;height:5px;background:var(--blue);display:block}
.f-social.active i{background:#fff}
.quick-links{position:absolute;left:226px;top:71px;list-style:none;font-size:7px;color:#a9a6a6}
.quick-links li{height:16.2px}
.field{position:absolute;background:var(--field);font-size:6.5px;color:#d0cece;padding:4px 7px}
.f-send{position:absolute;left:349px;top:172px;width:53px;height:18px;background:var(--blue);font-size:7px;display:flex;align-items:center;justify-content:center;gap:4px}
.copyright{position:absolute;left:50px;top:221px;font-size:7px;color:#a9a6a6}
.copyright span{color:var(--blue)}
.to-top{position:absolute;left:618px;top:216px}
</style>
</head>
<body>

<header class="site-header">
  <div class="brand">
    <div class="brand-name"><span class="brand-mark"></span>Lodvenra</div>
    <div class="brand-tag">Executive Accommodation</div>
  </div>
  <a class="btn btn-icon" aria-label="Call">
    <svg width="8" height="8" viewBox="0 0 10 10"><path d="M2 1l2 2-1 1.2c.6 1.2 1.6 2.2 2.8 2.8L7 6l2 2-1.2 1.2C4.5 9 1 5.5.8 2.2z" fill="none" stroke="#3276b5" stroke-width="1"/></svg>
  </a>
  <a class="btn btn-login"><svg width="6" height="6" viewBox="0 0 6 6"><circle cx="3" cy="1.8" r="1.5" fill="#fff"/><path d="M0 6c0-2 1.4-2.8 3-2.8S6 4 6 6z" fill="#fff"/></svg>Login / Sign Up</a>
  <a class="btn btn-schedule"><svg width="7" height="7" viewBox="0 0 7 7"><rect x=".5" y="1" width="6" height="5.5" fill="none" stroke="#3276b5"/><path d="M.5 2.8h6" stroke="#3276b5"/></svg>Schedule an Inspection</a>
</header>

<section class="gallery">
  <div class="photo photo-kitchen" role="img" aria-label="Photo of a bright modern kitchen with a window"></div>
  <div class="photo photo-bedroom" role="img" aria-label="Photo of the shared bedroom with two double beds and orange throws"></div>
  <div class="photo photo-wall" role="img" aria-label="Photo of a textured feature wall with a vase of flowers"></div>
  <span class="arrow arrow-left"><svg width="6" height="8" viewBox="0 0 6 8"><path d="M4 1L1 4l3 3" fill="none" stroke="#3276b5"/></svg></span>
  <span class="arrow arrow-right"><svg width="6" height="8" viewBox="0 0 6 8"><path d="M2 1l3 3-3 3" fill="none" stroke="#3276b5"/></svg></span>
</section>

<main>
  <section class="listing">
    <p class="address"><svg width="6" height="8" viewBox="0 0 6 8"><path d="M3 8C1 5 0 4 0 3a3 3 0 016 0c0 1-1 2-3 5z" fill="#3276b5"/><circle cx="3" cy="3" r="1" fill="#fff"/></svg>4415 Harlow Crest Dr, KV 48210 - USA</p>
    <a class="map-link">Show On Map</a>
    <h1 class="listing-title">1 BK Sharing Rooms for Women at ₹540 in Lorem, Ipsum, USA</h1>
    <p class="listing-meta">Only for Women &nbsp;|&nbsp; 1 bed available</p>
    <p class="price">Rental Price: <span>$ 540 - $ 640</span></p>
  </section>

  <div class="rule" style="top:406px"></div>
  <h2 class="section-title" style="left:50px;top:427px">House Amenities</h2>

  <div class="amenity" style="left:107px;top:459px">
    <svg width="22" height="18" viewBox="0 0 22 18" fill="none" stroke="#4a4a4a"><rect x="2" y="3" width="18" height="7"/><rect x="4" y="5" width="5" height="4"/><rect x="13" y="5" width="5" height="4"/><path d="M1 10h20v5H1zM2 15v2M20 15v2"/></svg>1 Bedroom</div>
  <div class="amenity" style="left:203px;top:459px">
    <svg width="22" height="18" viewBox="0 0 22 18" fill="none" stroke="#4a4a4a"><path d="M3 9h16v3a5 5 0 01-5 5H8a5 5 0 01-5-5zM6 17l-1 1M16 17l1 1M14 9V3a2 2 0 014 0"/><circle cx="16" cy="6" r="1"/></svg>1 Bathroom</div>
  <div class="amenity" style="left:308px;top:459px">
    <svg width="22" height="18" viewBox="0 0 22 18" fill="none" stroke="#4a4a4a"><path d="M5 9V3h12v6M3 8h3v5h10V8h3v7H3zM5 15v2M17 15v2"/></svg>Fully Furnished</div>
  <div class="amenity" style="left:411px;top:459px">
    <svg width="22" height="18" viewBox="0 0 22 18" fill="none" stroke="#4a4a4a"><path d="M2 8l9-6 9 6v9H2zM5 17v-6h12v6M6 14h10"/></svg>Street Parking</div>

  <div class="rule" style="top:514px"></div>
  <h2 class="section-title" style="left:50px;top:535px">Room Amenities</h2>

  <div class="room-item" style="left:50px;top:567px"><svg width="16" height="18" viewBox="0 0 16 18" fill="none" stroke="#4a4a4a"><path d="M3 17V1h10v16M1 17h14"/><circle cx="10" cy="9" r=".8"/></svg>Size of room - xxx sqm</div>
  <div class="room-item" style="left:198px;top:568px"><svg width="18" height="14" viewBox="0 0 18 14" fill="none" stroke="#4a4a4a"><rect x="2" y="1" width="14" height="6"/><path d="M1 7h16v4H1zM2 11v2M16 11v2"/></svg>Bed size - xx - xx ft</div>
  <div class="room-item" style="left:347px;top:567px"><svg width="18" height="16" viewBox="0 0 18 16" fill="none" stroke="#4a4a4a"><rect x="1" y="1" width="16" height="11"/><path d="M6 15h6M9 12v3"/></svg>TV</div>

  <div class="room-item" style="left:50px;top:598px"><svg width="16" height="18" viewBox="0 0 16 18" fill="none" stroke="#4a4a4a"><rect x="1" y="1" width="14" height="16"/><path d="M8 1v16M4 6v4"/></svg>Bathroom - Shared</div>
  <div class="room-item" style="left:198px;top:598px"><svg width="18" height="18" viewBox="0 0 18 18" fill="none" stroke="#4a4a4a"><circle cx="7" cy="6" r="4"/><path d="M1 17c0-4 3-6 6-6s6 2 6 6zM11 2.5a4 4 0 110 7M14 11c2 1 3 3 3 6"/></svg>Professionals - Housemates</div>
  <div class="room-item" style="left:347px;top:598px"><svg width="18" height="18" viewBox="0 0 18 18" fill="none" stroke="#4a4a4a"><path d="M1 9h16M2 9v8M16 9v8M4 9V3h6v6M7 5v1"/><rect x="11" y="4" width="5" height="5"/></svg>Workstation</div>

  <div class="room-item" style="left:50px;top:630px"><svg width="16" height="16" viewBox="0 0 16 16" fill="none" stroke="#4a4a4a"><circle cx="8" cy="8" r="7"/><path d="M3 3l10 10M4 8h8v2H4z"/></svg>Non-Smoking</div>
  <div class="room-item" style="left:198px;top:629px"><svg width="18" height="18" viewBox="0 0 18 18" fill="none" stroke="#4a4a4a"><circle cx="9" cy="7" r="1.5"/><path d="M9 9v8M6 4a4 4 0 000 6M12 4a4 4 0 010 6M3.5 1.5a8 8 0 000 11M14.5 1.5a8 8 0 010 11"/></svg>High Speed Internet</div>
  <div class="room-item" style="left:347px;top:629px"><svg width="18" height="18" viewBox="0 0 18 18" fill="none" stroke="#4a4a4a"><path d="M2 9h14v2a5 5 0 01-5 5H7a5 5 0 01-5-5zM12 9V3a2 2 0 014 0"/><circle cx="14" cy="6" r="1"/></svg>Ensuite Shower</div>

  <div class="room-item" style="left:50px;top:661px"><svg width="18" height="18" viewBox="0 0 18 18" fill="none" stroke="#4a4a4a"><rect x="1" y="1" width="6" height="5"/><rect x="10" y="1" width="7" height="5"/><path d="M1 9h16v8H1zM9 9v8M4 12h2M12 12h2"/></svg>Kitchenette</div>
  <div class="room-item" style="left:198px;top:661px"><svg width="18" height="18" viewBox="0 0 18 18" fill="none" stroke="#4a4a4a"><rect x="4" y="1" width="10" height="16"/><path d="M4 5h10M4 12h10M9 5v7"/></svg>Wardrobe</div>
  <div class="room-item" style="left:347px;top:661px"><svg width="18" height="18" viewBox="0 0 18 18" fill="none" stroke="#4a4a4a"><rect x="1" y="1" width="16" height="16"/><path d="M1 6.5h16M1 12h16M9 1v16"/></svg>Storage Space</div>

  <div class="rule" style="top:702px"></div>

  <aside>
    <div class="sidebar"></div>
    <div class="avatar"><div class="avatar-photo" role="img" aria-label="Host profile photo"></div></div>
    <p class="host-name">Mara Ellison</p>
    <p class="host-role">Contrary popular</p>
    <div class="message-box">Write A Message ...</div>
    <a class="btn-send"><svg width="7" height="6" viewBox="0 0 7 6"><path d="M0 0l7 3-7 3 1-3z" fill="#fff"/></svg>Send Message</a>
    <div class="side-rule" style="top:536px"></div>
    <p class="side-title" style="top:553px">Contact Info</p>
    <p class="side-text" style="top:575px">Call Us: 555 - 318 - 2046</p>
    <p class="side-text" style="top:586px"><a>info@lodvenra.com</a></p>
    <div class="side-rule" style="top:613px"></div>
    <p class="side-title" style="top:630px">Share to a Friend</p>
    <a class="share-box" style="left:498px" aria-label="Share link one"><i></i></a>
    <a class="share-box" style="left:522px" aria-label="Share link two"><i></i></a>
    <a class="share-box" style="left:546px" aria-label="Share link three"><i></i></a>
    <a class="share-box" style="left:570px" aria-label="Share link four"><i></i></a>
    <a class="share-box" style="left:594px" aria-label="Share link five"><i></i></a>
  </aside>

  <h2 class="section-title" style="left:0;width:679px;text-align:center;top:722px">Public Amenities..</h2>
  <div class="amenity" style="left:116px;top:753px">
    <svg width="18" height="20" viewBox="0 0 18 20" fill="none" stroke="#4a4a4a"><rect x="3" y="1" width="12" height="14" rx="3"/><path d="M3 8h12M6 18l-2 2M12 18l2 2M5 15l-1 3h10l-1-3"/><circle cx="6" cy="12" r=".8"/><circle cx="12" cy="12" r=".8"/></svg>Trains Station</div>
  <div class="amenity" style="left:265px;top:753px">
    <svg width="20" height="20" viewBox="0 0 20 20" fill="none" stroke="#4a4a4a"><rect x="6" y="2" width="12" height="15" rx="2"/><path d="M6 10h12M8 17v2M16 17v2M3 4v15"/><circle cx="3" cy="4" r="2"/></svg>Busses Station</div>
  <div class="amenity" style="left:414px;top:753px">
    <svg width="18" height="20" viewBox="0 0 18 20" fill="none" stroke="#4a4a4a"><path d="M1 19h16M3 19V8h5v11M8 19V2h7v17M10 5h3M10 8h3M10 11h3M10 14h3M5 11h1M5 14h1"/></svg>Distance to the City</div>
  <div class="amenity" style="left:564px;top:753px">
    <svg width="18" height="20" viewBox="0 0 18 20" fill="none" stroke="#4a4a4a"><path d="M9 16C5 11 3 9 3 6.5a6 6 0 0112 0C15 9 13 11 9 16z"/><circle cx="9" cy="6.5" r="2"/><path d="M4 15l-3 4h16l-3-4"/></svg>MAP of the Area</div>

  <div class="area-map" role="img" aria-label="Map of the surrounding area in the central United States"></div>
</main>

<footer class="site-footer">
  <h3 class="f-heading" style="left:50px">Contact Us</h3>
  <p class="f-phone">555 - 318 - 2046</p>
  <p class="f-small" style="left:50px;top:86px;color:#c9c6c6">info@lodvenra.com</p>
  <p class="f-small" style="left:50px;top:104px">4415 Harlow Crest Blvd<br>Brennick, KV 48210</p>
  <a class="f-link">Get A Directions</a>
  <a class="f-social" style="left:50px" aria-label="Social link one"><i></i></a>
  <a class="f-social active" style="left:72px" aria-label="Social link two"><i></i></a>
  <a class="f-social" style="left:94px" aria-label="Social link three"><i></i></a>
  <a class="f-social" style="left:117px" aria-label="Social link four"><i></i></a>

  <h3 class="f-heading" style="left:226px">Quick Links</h3>
  <ul class="quick-links">
    <li>Home</li><li>About Us</li><li>Services</li><li>Portfolio</li><li>Testimonials</li><li>News</li><li>Contact Us</li>
  </ul>

  <h3 class="f-heading" style="left:349px">How Can We Help?</h3>
  <div class="field" style="left:349px;top:68px;width:135px;height:18px">Name</div>
  <div class="field" style="left:493px;top:68px;width:136px;height:18px">Phone</div>
  <div class="field" style="left:349px;top:96px;width:280px;height:17px">Email</div>
  <div class="field" style="left:349px;top:123px;width:280px;height:41px">Message</div>
  <a class="f-send"><svg width="7" height="6" viewBox="0 0 7 6"><path d="M0 0l7 3-7 3 1-3z" fill="#fff"/></svg>Send</a>

  <p class="copyright">© 2019 <span>Lodvenra</span>. All rights reserved.</p>
  <svg class="to-top" width="12" height="13" viewBox="0 0 12 13" aria-label="Back to top"><path d="M6 0l6 13-6-4-6 4z" fill="#3276b5"/></svg>
</footer>

</body>
</html>
```